Business Card Design for New Game Studio

We need a business card design. We are a new company developing innovative mobile and platform games.

I would like to see very innovative design thats brings out the company's goal and direction.

My Company's goal and direction is to "Evolve the way of gaming, Bring fun and entertainment to all gamers"

Please do use our company logo which I have attached to be included in the design.

Please put in details for name, title, contacts etc ... be creative !!!

Reason: Company logo redesign. Awaiting it. Thanks

Hi all Please do wait for my updated company logo. Thanks

Reason: Still waiting on new company logo. Thanks all

Hi All Designers .... Sorry for the long wait... Please see the new file for my new company logo uploaded. Waiting to see all your creative design. Cheers

Hi All .... Please do not just mass send a whole bunch of similar designs .... Would like to see quality instead of quantity Cheers

Entertainment

```html
<!DOCTYPE html>
<html lang="en">
<head>
<meta charset="utf-8">
<title>Shiftplay Studio – Business Card</title>
<link rel="stylesheet" href="https://fonts.googleapis.com/css2?family=Roboto+Condensed:wght@400;700&display=swap">
<style>
  :root {
    --page: #ffffff;
    --card: #ffffff;
    --card-edge: #9a9a9a;
    --charcoal: #3f3f41;
    --lime: #cddc1e;
    --ink: #3a3a3a;
    --light-text: #f2f2f2;
  }
  * { box-sizing: border-box; margin: 0; padding: 0; }
  html, body {
    width: 1200px;
    height: 442px;
    overflow: hidden;
    background: var(--page);
    font-family: "Roboto Condensed", "Arial Narrow", sans-serif;
  }
  .canvas {
    position: relative;
    width: 1200px;
    height: 442px;
  }
  .card {
    position: absolute;
    top: 76px;
    width: 475px;
    height: 291px;
    background: var(--card);
    border: 1px solid var(--card-edge);
    overflow: hidden;
  }
  .card--front { left: 88px; }
  .card--back { left: 632px; }

  .brand-block {
    position: absolute;
    left: 40px;
    top: 0;
    width: 142px;
    height: 99px;
    background: var(--charcoal);
    display: flex;
    align-items: center;
    justify-content: center;
    gap: 6px;
  }
  .brand-mark {
    width: 9px;
    height: 9px;
    background: var(--lime);
  }
  .brand-name {
    color: var(--lime);
    font-weight: 700;
    font-size: 13px;
    letter-spacing: 0.2px;
  }

  .identity-line {
    position: absolute;
    left: 38px;
    top: 179px;
    font-size: 13px;
    font-weight: 700;
    color: var(--ink);
    letter-spacing: 0.2px;
    white-space: nowrap;
  }
  .identity-line .divider { margin: 0 9px; font-weight: 400; }

  .accent-band {
    position: absolute;
    left: 0;
    top: 207px;
    width: 475px;
    height: 84px;
  }

  .contact-block,
  .tagline {
    position: absolute;
    left: 38px;
    color: var(--light-text);
    font-size: 11px;
    line-height: 17px;
    white-space: nowrap;
  }
  .contact-block { top: 225px; }
  .tagline { top: 227px; font-size: 11.5px; line-height: 18px; }
</style>
</head>
<body>
<div class="canvas">

  <section class="card card--front">
    <div class="brand-block">
      <span class="brand-mark"></span>
      <span class="brand-name">Shiftplay Studio</span>
    </div>

    <p class="identity-line">NAME OF PERSON<span class="divider">I</span>DESIGNATION<span class="divider">I</span>MOBILE NO</p>

    <svg class="accent-band" viewBox="0 0 475 84" aria-hidden="true">
      <rect x="0" y="4" width="475" height="80" fill="var(--charcoal)"/>
      <rect x="0" y="0" width="475" height="2" fill="var(--lime)"/>
      <polygon points="362,0 475,0 475,8 370,8" fill="var(--lime)"/>
    </svg>

    <div class="contact-block">
      <p>ADDRESS : number, street, area, place name, pincode</p>
      <p>info@shiftplaystudio.com, designation@shiftplaystudio.com</p>
      <p>phone numbers of the company</p>
    </div>
  </section>

  <section class="card card--back">
    <div class="brand-block">
      <span class="brand-mark"></span>
      <span class="brand-name">Shiftplay Studio</span>
    </div>

    <svg class="accent-band" viewBox="0 0 475 84" aria-hidden="true">
      <rect x="0" y="4" width="475" height="80" fill="var(--charcoal)"/>
      <rect x="0" y="0" width="475" height="2" fill="var(--lime)"/>
      <polygon points="362,0 475,0 475,8 370,8" fill="var(--lime)"/>
    </svg>

    <p class="tagline">Evolve the way of gaming, Bring fun and entertainment to all gamersEvolve<br>the way of gaming, Bring fun and entertainment to all gamers</p>
  </section>

</div>
</body>
</html>
```